Book Cover Design - Business/Self-Help Book

Book cover design for a business/self-help book. The title of the book is "OTTER Compass - Seven Quiet Habits of Steady Growth" It should also have "Unlock the Nine Hidden Keys Behind Lasting Momentum" as a subtitle somewhere.

Please see the website for an idea of the logo and sub-words: http://www.ottercompassbook.com

Book size will be 8.5" x 5.25"
Author info: Marlo Quindt

If your design includes a shark on the cover, it MUST be a hammerhead shark. Logo is attached.

I would like to stick with a red or orange theme like on the website but am open to any color idea. I like brighter colors and want the book to stand out and be attractive. If it's white, the wording and logo should be a bright color.

The back cover will just be preview text and selling points. It could have a picture in the background but will not have any pictures of the author.

If you include a spine design, please put the hammerhead logo on the spine.

Target Market(s)

Young Entrepreneurs and Business Professionals

Industry/Entity Type

Business

Requirements
Must have
• The hammerhead shark logo
Nice to have
• Look at the website - http://www.ottercompassbook.com
• It would be nice to have the six words throughout the cover similar to how it shows on the website cover picture.
Should not have
• Even though it caters to a younger crowd, it should not be cartoonish or child-like. Want a more serious and modern feel. Not too cluttered, i want the title to stand out and the shark to stand out.

```html
<!DOCTYPE html>
<html lang="en">
<head>
<meta charset="utf-8">
<title>OTTER Compass – Book Cover Spread</title>
<link rel="stylesheet" href="https://fonts.googleapis.com/css2?family=Nunito+Sans:wght@300;400;600;700;800&display=swap">
<style>
  :root {
    --bg: #ece8e4;
    --paper: #ffffff;
    --ink: #1a1a1a;
    --yellow: #ffc21a;
    --lime: #e6ea5a;
    --orange: #ff9a12;
    --orange-deep: #f26a1b;
    --red: #f0324a;
    --pink: #ff2a7a;
    --magenta: #f02aa6;
    --spine-line: #b9d3d6;
  }
  * { box-sizing: border-box; margin: 0; padding: 0; }
  html, body { width: 1200px; height: 1000px; overflow: hidden; }
  body {
    background: var(--bg);
    font-family: "Nunito Sans", Arial, sans-serif;
    position: relative;
  }
  .spread {
    position: absolute;
    left: 117px; top: 140px;
    width: 964px; height: 730px;
    background: var(--paper);
    box-shadow: 0 2px 6px rgba(0,0,0,.25);
  }
  .panel { position: absolute; top: 0; height: 730px; overflow: hidden; }

  /* Back cover */
  .back { left: 0; width: 449px; }
  .back-band-top {
    position: absolute; left: 0; top: 0; width: 100%; height: 56px;
    background: linear-gradient(100deg, #ffb61c 0%, var(--yellow) 45%, #ffae18 100%);
  }
  .back-band-bottom {
    position: absolute; left: 0; bottom: 0; width: 100%; height: 143px;
    background: linear-gradient(20deg, var(--pink) 0%, #ff5a4a 28%, var(--orange) 60%, #ff9e16 100%);
  }
  .back-title { position: absolute; left: 0; top: 92px; width: 100%; text-align: center; }
  .back-title .word-main {
    display: block; font-weight: 300; font-size: 58px; line-height: 1;
    color: var(--orange); letter-spacing: 1px;
  }
  .back-title .word-sub {
    display: block; font-weight: 700; font-size: 28px; line-height: 1;
    color: var(--orange-deep); letter-spacing: 8px; margin-top: 4px;
  }
  .back-title .tagline {
    display: block; font-weight: 600; font-size: 12px; color: var(--red); margin-top: 6px;
  }
  .blurb { position: absolute; left: 45px; top: 239px; width: 380px; }
  .blurb p {
    font-size: 12.5px; font-weight: 600; color: var(--ink);
    line-height: 24px; margin-bottom: 20px; white-space: nowrap;
  }

  /* Spine */
  .spine { left: 449px; width: 66px; }
  .spine-art {
    position: absolute; left: 0; top: 56px; width: 100%; height: 531px;
    background: linear-gradient(180deg, #f2b81e 0%, var(--orange) 40%, #ff9a12 75%, #ffa61a 100%);
  }
  .spine-title {
    position: absolute; left: 0; top: 56px; width: 100%; height: 531px;
    display: flex; align-items: center; justify-content: center;
  }
  .spine-title .vertical {
    writing-mode: vertical-rl; transform: rotate(180deg);
    color: #fff; text-align: center; white-space: nowrap;
  }
  .spine-title .name { font-weight: 300; font-size: 30px; letter-spacing: 3px; line-height: 1; }
  .spine-title .tagline { font-weight: 600; font-size: 11px; letter-spacing: 1px; margin-right: 6px; }
  .spine-mark {
    position: absolute; left: 0; top: 628px; width: 100%;
    display: flex; flex-direction: column; align-items: center; gap: 4px;
  }
  .spine-mark .dot { width: 12px; height: 12px; border-radius: 50%; background: var(--red); }
  .spine-mark .name { font-size: 10px; font-weight: 700; color: var(--red); letter-spacing: 1px; }
  .spine-fold { position: absolute; left: 513px; top: 0; width: 1px; height: 730px; background: var(--spine-line); }

  /* Front cover */
  .front { left: 515px; width: 449px; }
  .front-art {
    position: absolute; left: 0; top: 56px; width: 100%; height: 531px;
    background:
      radial-gradient(circle at 100% 0%, var(--lime) 0%, rgba(255,200,40,.6) 18%, rgba(255,170,20,0) 40%),
      linear-gradient(170deg, #ffa414 0%, var(--orange) 40%, #ff7a2a 68%, #ff3e55 88%, var(--pink) 100%);
  }
  .front-art svg { position: absolute; inset: 0; }
  .front-title { position: absolute; left: 0; top: 174px; width: 100%; padding-left: 86px; padding-right: 82px; }
  .front-title .word-main {
    display: block; font-weight: 300; font-size: 84px; line-height: 1;
    color: #fff; letter-spacing: 2px;
  }
  .front-title .word-sub {
    display: block; font-weight: 700; font-size: 40px; line-height: 1;
    color: #fff; letter-spacing: 13px; margin-top: 2px;
  }
  .front-title .tagline {
    display: block; font-weight: 600; font-size: 15px; color: #fff; margin-top: 6px; white-space: nowrap;
  }
  .front-subtitle {
    position: absolute; left: 0; top: 556px; width: 100%; text-align: center;
    font-size: 14px; font-weight: 600; color: #fff; letter-spacing: .4px; white-space: nowrap;
  }
  .elements {
    position: absolute; left: 0; top: 595px; width: 100%;
    display: flex; justify-content: space-between; padding: 0 14px 0 18px;
    font-size: 11px; font-weight: 700; letter-spacing: .6px;
  }
  .elements li { list-style: none; }
  .elements li:nth-child(1) { color: #ffab1e; }
  .elements li:nth-child(2) { color: #ff8a22; }
  .elements li:nth-child(3) { color: #ff6a2e; }
  .elements li:nth-child(4) { color: var(--red); }
  .elements li:nth-child(5) { color: #f42a78; }
  .elements li:nth-child(6) { color: var(--magenta); }
  .author {
    position: absolute; left: 0; top: 672px; width: 100%; text-align: center;
    font-size: 18px; font-weight: 600; color: var(--red);
  }
</style>
</head>
<body>
  <main class="spread">
    <section class="panel back">
      <div class="back-band-top"></div>
      <h2 class="back-title">
        <span class="word-main">OTTER</span>
        <span class="word-sub">COMPASS</span>
        <span class="tagline">Seven Quiet Habits of Steady Growth</span>
      </h2>
      <div class="blurb">
        <p>Text text tex text text text text text text text text text text text<br>Text text tex text text text text text text text text text text text<br>Text text tex text text text text text text text text text text text</p>
        <p>Text text tex text text text text text text text text text text text<br>Text text tex text text text text text text text text text text text<br>Text text tex text text text text text text text text text text text<br>Text text tex text text text text text text text text text text text</p>
        <p>Text text tex text text text text text text text text text text text<br>Text text tex text text text text text text text text text text text<br>Text text tex text text text text text text text text text text text</p>
      </div>
      <div class="back-band-bottom"></div>
    </section>

    <section class="panel spine">
      <div class="spine-art"></div>
      <div class="spine-title">
        <div class="vertical">
          <span class="name">OTTER COMPASS</span><br>
          <span class="tagline">Seven Quiet Habits of Steady Growth</span>
        </div>
      </div>
      <div class="spine-mark">
        <span class="dot"></span>
        <span class="name">OTTER</span>
      </div>
    </section>
    <div class="spine-fold"></div>

    <section class="panel front">
      <div class="front-art">
        <svg width="449" height="531" viewBox="0 0 449 531" aria-hidden="true">
          <polygon points="0,0 160,0 0,220" fill="#fff" opacity=".06"/>
          <polygon points="449,80 449,330 230,531 120,531" fill="#fff" opacity=".05"/>
          <polygon points="200,0 330,0 230,531 150,531" fill="#fff" opacity=".04"/>
          <polygon points="0,300 0,531 110,531" fill="#ffd040" opacity=".08"/>
        </svg>
      </div>
      <h1 class="front-title">
        <span class="word-main">OTTER</span>
        <span class="word-sub">COMPASS</span>
        <span class="tagline">Seven Quiet Habits of Steady Growth</span>
      </h1>
      <p class="front-subtitle">Unlock the Nine Hidden Keys Behind Lasting Momentum</p>
      <ul class="elements">
        <li>TALENT</li><li>ROUTINE</li><li>GOAL</li><li>PARTNERSHIPS</li><li>INSIGHT</li><li>VALUES</li>
      </ul>
      <p class="author">Marlo Quindt</p>
    </section>
  </main>
</body>
</html>
```